BRIVETTA Need a luxury modern business card designed.

Need a luxury modern business card designed. refer to the uploaded files for the company name and logo in the zip file under source files. i will making my descion on monday. so please send in before then so if we need to edit we will have the time. we have a trade show coming up and im on a deadline for printer.

Target Market(s)

high end clients

Contact Information for Business Card

Company nAme and logo. Calvin Moross Co-Founder / Project Manager Office # 416-555-7391 Cell # 416-555-0186 BRIVETTA.CA Calvin@brivetta.ca

Font styles to use
Other font styles liked:
• Modern

Requirements
Must have
• Company name and logo, contact info, using the black, gold and white color scheme.

```html
<!DOCTYPE html>
<html lang="en">
<head>
<meta charset="utf-8">
<title>Brivetta Business Card</title>
<link rel="stylesheet" href="https://fonts.googleapis.com/css2?family=Jost:wght@400;500&display=swap">
<style>
  :root {
    --backdrop: #808184;
    --card-black: #0d0d0d;
    --card-mid: #3a3a3a;
    --gold: #d3a52c;
    --gold-text: #b39a5e;
    --white: #ffffff;
  }
  * { margin: 0; padding: 0; box-sizing: border-box; }
  html, body { width: 1071px; height: 1200px; overflow: hidden; }
  body {
    background: var(--backdrop);
    font-family: "Jost", "Futura", sans-serif;
    position: relative;
  }
  .card {
    position: absolute;
    left: 212px;
    width: 657px;
    height: 376px;
    overflow: hidden;
    background: radial-gradient(ellipse at 50% 45%, var(--card-mid) 0%, #1e1e1e 45%, var(--card-black) 100%);
    box-shadow: 0 14px 14px -8px rgba(0,0,0,0.35);
  }
  .card--front { top: 172px; }
  .card--back { top: 663px; }
  .card__band { position: absolute; inset: 0; width: 100%; height: 100%; }

  .brand {
    position: absolute;
    left: 0; right: 0;
    top: 202px;
    text-align: center;
    color: var(--white);
    font-size: 44px;
    font-weight: 400;
    line-height: 1;
  }

  .person { position: absolute; left: 52px; top: 48px; }
  .person__name {
    color: var(--white);
    font-size: 37px;
    font-weight: 400;
    line-height: 1;
  }
  .person__role {
    color: var(--gold-text);
    font-size: 17px;
    font-weight: 500;
    line-height: 1.6;
    margin-top: 8px;
  }
  .contact {
    position: absolute;
    display: flex;
    align-items: center;
    gap: 18px;
    color: var(--white);
    font-size: 17px;
    line-height: 1;
    white-space: nowrap;
  }
  .contact__icon { width: 20px; height: 20px; flex: none; }
  .contact--office { left: 318px; top: 189px; }
  .contact--cell { left: 266px; top: 238px; }
  .contact--web { left: 208px; top: 283px; word-spacing: 4px; }
</style>
</head>
<body>

<section class="card card--front" aria-label="Card front">
  <svg class="card__band" viewBox="0 0 425 244" preserveAspectRatio="none" role="img" aria-label="Plain gold diagonal bands across two corners">
    <defs>
      <linearGradient id="goldFront" x1="0" y1="1" x2="1" y2="0">
        <stop offset="0" stop-color="#b8891c"/>
        <stop offset="0.5" stop-color="#f2cd5e"/>
        <stop offset="1" stop-color="#c99a26"/>
      </linearGradient>
    </defs>
    <polygon points="0,0 170,0 0,130" fill="#080808"/>
    <polygon points="170,0 222,0 0,150 0,130" fill="url(#goldFront)"/>
    <polygon points="425,244 425,140 290,244" fill="#080808"/>
    <polygon points="425,122 425,140 290,244 262,244" fill="url(#goldFront)"/>
  </svg>
  <div class="brand">BRIVETTA</div>
</section>

<section class="card card--back" aria-label="Card back">
  <svg class="card__band" viewBox="0 0 425 244" preserveAspectRatio="none" role="img" aria-label="Plain gold diagonal band">
    <defs>
      <linearGradient id="goldBack" x1="0" y1="1" x2="1" y2="0">
        <stop offset="0" stop-color="#b8891c"/>
        <stop offset="0.5" stop-color="#e6bc45"/>
        <stop offset="1" stop-color="#f5d264"/>
      </linearGradient>
    </defs>
    <polygon points="0,0 298,0 0,224" fill="#141414"/>
    <polygon points="298,0 354,0 24,244 0,244 0,224" fill="url(#goldBack)"/>
  </svg>
  <div class="person">
    <h1 class="person__name">Calvin Moross</h1>
    <p class="person__role">Co-Founder<br>Project Manager</p>
  </div>
  <p class="contact contact--office">
    <svg class="contact__icon" viewBox="0 0 20 20" aria-hidden="true">
      <path d="M5,3 c1.2,-0.7 2.2,0 2.8,1.1 l1.2,2 c0.5,0.9 0.2,1.7 -0.6,2.2 l-1,0.6 c0.6,1.8 1.8,3.5 3.5,4.6 l1,-0.6 c0.7,-0.5 1.7,-0.2 2.2,0.5 l1.2,2 c0.6,1.1 0.5,2.2 -0.7,2.8 c-4.9,2.4 -11.5,-7.8 -9.6,-15.2 z" fill="var(--gold)"/>
    </svg>
    <span>416-555-7391</span>
  </p>
  <p class="contact contact--cell">
    <svg class="contact__icon" viewBox="0 0 20 20" aria-hidden="true">
      <rect x="5.5" y="1.5" width="9" height="17" rx="1.8" fill="none" stroke="var(--gold)" stroke-width="1.6"/>
      <rect x="8.5" y="15" width="3" height="1.3" fill="var(--gold)"/>
    </svg>
    <span>416-555-0186</span>
  </p>
  <p class="contact contact--web">
    <svg class="contact__icon" viewBox="0 0 20 20" aria-hidden="true">
      <circle cx="10" cy="10" r="9.5" fill="var(--gold)"/>
      <text x="10" y="14" text-anchor="middle" font-family="Jost, sans-serif" font-size="12" font-weight="500" fill="#1c1c1c">@</text>
    </svg>
    <span>BRIVETTA.CA Calvin@brivetta.ca</span>
  </p>
</section>

</body>
</html>
```